Marwick barber salon has created a lotion and needs help titling.Loma by marwick ?Marwi

The product is for a lotion bottle , my prototype lotion bottle size is an 8oz black lotion bottle with pump. I want the label in florescent green. It should tap into the emotion of potential buyers. The design should say choose me 😀(not literally ). Though the text should be clear and punchy . I.e " the skin multi-vitamin." I'm looking for a designer intrigued by the thought of my lotion. The label should be georgeous,informative, with visuals that immediately convey what my product is and how it works.Not distracting, but clear and punchy, with no expectation of someone to read more than a couple of words.The text should support the visual in a way the visual could not. It seems that nowadays visuals are taking over with very little text. The font,color , or punch of color should be enticing.
So here are some particular ideas of points about the lotion that could possibly be put on back as is done by lotion makers.
.ingredients
.ZNT approved
.portion of proceeds go to bright path fund
.TC circled ( which is for pending trademark)
. I would like the word New in fluorescent on the bottle
.P.O Box address of place of manufacturing product.
. To help skin stay slightly moist,soft,and flexible with a smooth fine grained texture.

its a lotion so I want it available for all

Barber

9bcb3c

• the word" Loma" and By marwick...the word new on the bottle visible

```html
<!DOCTYPE html>
<html lang="en">
<head>
<meta charset="utf-8">
<title>Loma by marwick – Skin Multi-Vitamin Lotion Label</title>
<link href="https://fonts.googleapis.com/css2?family=Questrial&family=Raleway:wght@500;600;700;800&display=swap" rel="stylesheet">
<style>
  :root{
    --page:#ececec;
    --white:#ffffff;
    --green-dark:#62941c;
    --green-mid:#8cbd3a;
    --green-bright:#9bcb3c;
    --green-soft:#b5da6e;
    --green-pale:#cfe79c;
    --orange:#f7a21b;
  }
  *{box-sizing:border-box;margin:0;padding:0}
  html,body{width:1200px;height:857px;overflow:hidden;background:var(--page)}
  body{font-family:"Raleway",sans-serif;position:relative}
  .label{position:absolute;left:55px;top:145px;width:1090px;height:570px;background:var(--white);overflow:hidden;box-shadow:0 2px 10px rgba(0,0,0,.18)}
  .label-waves{position:absolute;left:0;top:0;width:1090px;height:570px}

  .new-badge{position:absolute;border-radius:50%;background:var(--green-bright);color:var(--white);font-weight:800;display:flex;align-items:center;justify-content:center;letter-spacing:.5px;box-shadow:inset 0 -4px 0 var(--green-mid)}
  .new-badge--back{left:122px;top:16px;width:54px;height:54px;font-size:13px}
  .new-badge--front{left:634px;top:16px;width:80px;height:80px;font-size:20px}

  .brand-name{position:absolute;font-family:"Questrial",sans-serif;color:var(--green-bright);line-height:1;font-weight:400}
  .brand-name--back{left:166px;top:64px;font-size:74px}
  .brand-name--front{left:652px;top:110px;font-size:118px}
  .brand-byline{position:absolute;color:var(--orange);font-weight:800;letter-spacing:.2px}
  .brand-byline--back{left:172px;top:141px;font-size:10.5px}
  .brand-byline--front{left:659px;top:236px;font-size:15px}

  .panel{position:absolute;border-radius:10px;background:var(--green-mid);color:var(--white);font-weight:600}
  .panel--intro{left:53px;top:162px;width:440px;height:66px;padding:10px 14px;font-size:12.4px;line-height:16px;text-align:center}
  .panel--about{left:53px;top:240px;width:236px;height:230px;padding:10px 12px;font-size:12.2px;line-height:16px;text-align:justify}
  .panel--ingredients{left:297px;top:291px;width:196px;height:149px;padding:9px 12px;font-size:12px;line-height:16px}
  .panel--ingredients h3{font-size:12.5px;font-weight:800;margin-bottom:8px}
  .proceeds{position:absolute;left:297px;top:239px;width:193px;height:44px;border:1.5px solid var(--green-mid);border-radius:10px;background:var(--white);color:var(--green-bright);font-weight:800;font-size:11.5px;line-height:15px;text-align:center;padding-top:6px}
  .best-before{position:absolute;left:297px;top:448px;width:196px;height:22px;border:1.5px solid var(--white);color:var(--white);font-weight:700;font-size:11.5px;text-align:center;line-height:19px}

  .barcode-area{position:absolute;left:53px;top:488px;width:135px;height:67px;background:var(--white);color:var(--green-mid);font-weight:700;font-size:10.5px;display:flex;align-items:center;justify-content:center}
  .recycle-mark{position:absolute;left:212px;top:495px;width:50px;height:50px}
  .contact{position:absolute;left:280px;top:487px;color:var(--white);font-weight:700;font-size:10.6px;line-height:15px;font-style:normal}

  .product-type{position:absolute;left:662px;top:279px;width:312px;height:35px;border-radius:8px;background:var(--green-mid);border:2px solid var(--green-pale);color:var(--white);font-weight:800;font-size:16.5px;text-align:center;line-height:31px}
  .spanish-line{position:absolute;left:682px;top:322px;width:272px;color:var(--green-bright);font-weight:700;font-size:12.8px;line-height:17px;text-align:center}
  .claim{position:absolute;left:600px;top:450px;width:436px;color:var(--white);font-weight:800;font-size:19px;line-height:26px;text-align:center}
  .directions{position:absolute;left:600px;top:508px;width:436px;color:var(--white);font-weight:700;font-size:10px;text-align:center}
  .net-weight{position:absolute;left:600px;top:527px;width:436px;color:var(--white);font-weight:700;font-size:17px;text-align:center}
</style>
</head>
<body>
<main class="label">
  <svg class="label-waves" viewBox="0 0 1090 570" aria-hidden="true">
    <path fill="#d2e9a2" d="M0 245 C150 220 300 262 420 258 C600 252 700 330 830 352 C950 372 1040 335 1090 300 L1090 570 L0 570Z"/>
    <path fill="#b5da6e" d="M0 292 C150 262 250 252 330 292 C450 332 500 300 560 330 C700 402 900 392 1090 332 L1090 570 L0 570Z"/>
    <path fill="#98c745" d="M0 340 L170 292 L330 350 L470 305 L620 372 C760 410 900 400 1090 360 L1090 570 L0 570Z"/>
    <path fill="#62941c" d="M0 438 C200 418 400 458 600 440 C800 422 950 404 1090 420 L1090 570 L0 570Z"/>
  </svg>

  <div class="new-badge new-badge--back">NEW</div>
  <div class="brand-name brand-name--back">Loma</div>
  <div class="brand-byline brand-byline--back">BY MARWICK</div>

  <p class="panel panel--intro">Loma multi-vitamin lotion, supplies the skin with the nutrients needed for daily skin health. With vitamins (A,C,D,E) that repair, replenish, and promote general skin health.</p>

  <p class="panel panel--about">Dermatologist describe healthy skin as slightly moist, soft, and flexible and its texture is smooth and fine grained. Loma lotion is designed with this goal in mind. That is because at "Loma" we know the importance of healthy skin. Our skin is our first line of defense against bacteria, minor injuries, chemical substances and temperature. With this in mind, we at Loma by marwick have engineered this product.</p>

  <p class="proceeds">PORTION OF PROCEEDS<br>GO TO BRIGHT PATH FUND</p>

  <section class="panel panel--ingredients">
    <h3>INGREDIENTS:</h3>
    <p>Distilled Water (H2O), Grapeseed oil, Coconut oil, Jojoba oil, Beeswax, Vita-A, Vita-C, Vita-D, Vita-E, Aloe Vera, Potassium sorbate, Honey, Glycerin, Stearic acid, Citric acid.</p>
  </section>

  <div class="best-before">Best Before: _ _ : _ _ : _ _ _ _</div>

  <div class="barcode-area">BARCODE</div>

  <svg class="recycle-mark" viewBox="0 0 50 50" aria-hidden="true">
    <circle cx="25" cy="25" r="21" fill="none" stroke="#ffffff" stroke-width="4"/>
  </svg>

  <address class="contact">
    QUESTIONS OR CONCERNS:<br>
    marwickbarbersalon@example.com<br>
    4821 Alder Lane<br>
    Fairview ca 90000<br>
    (555)014-2270 (555)018-3391
  </address>

  <div class="new-badge new-badge--front">NEW</div>
  <h1 class="brand-name brand-name--front">Loma</h1>
  <div class="brand-byline brand-byline--front">BY MARWICK</div>

  <h2 class="product-type">THE SKIN MULTI-VITAMIN LOTION</h2>
  <p class="spanish-line">Loma de Marwick, la piel multi vitaminas loción, mantiene la piel suave, lisa y ligeramente húmeda</p>

  <p class="claim">KEEPS SKIN SOFT,<br>SMOOTH AND SLIGHTLY MOIST</p>
  <p class="directions">Directions : For best results apply daily as needed to clean skin</p>
  <p class="net-weight">Net Weight: 8oz</p>
</main>
</body>
</html>
```